Marriage Podcast Needs Cover Art

The name of the marriage podcast is "Lanterns at Dusk", representing a bond between the husband, wife, and God. The artwork needs to include a rope tied in a heart shape and the podcast name (Lanterns at Dusk). I prefer a simple background, but a subtle pattern would be okay too. In general, simplicity is better. The artwork should be easy on the eyes. This cover art is what my listeners will see in their podcast app next to each episode name. The image is small, so the text needs to be large enough to read in this context. This means there will not be enough room for large pockets of blank space. The design basically fills the entire canvas.

Please see the attachment for some suggestions. Thanks! :)

Target Market(s)

Young married couples

Industry/Entity Type

Rope

Requirements
Must have
• - Rope tied in a heart shape.
• - Text: "Lanterns at Dusk"
• - 1400 x 1400 pixels
Nice to have
• - Bright or warm colors that convey love/marriage
• - 3000 x 3000 pixels
Should not have
• Dark or muted-color background

```html
<!DOCTYPE html>
<html lang="en">
<head>
<meta charset="utf-8">
<title>Lanterns at Dusk — Podcast Cover</title>
<link rel="stylesheet" href="https://fonts.googleapis.com/css2?family=Crimson+Pro:wght@700&display=swap">
<style>
  :root {
    --cream: #f3f1dc;
    --pattern-tone: #ebe8cf;
    --title-red: #b11916;
    --rope-red: #c63c3c;
    --rope-tan: #d4a766;
  }
  html, body {
    margin: 0;
    padding: 0;
    width: 1200px;
    height: 1200px;
    overflow: hidden;
    background: var(--cream);
  }
  .cover {
    position: relative;
    width: 1200px;
    height: 1200px;
    background: linear-gradient(180deg, var(--cream) 0%, var(--pattern-tone) 50%, var(--cream) 100%);
    overflow: hidden;
  }
  .rope-heart {
    position: absolute;
    left: 0;
    top: 0;
    width: 1200px;
    height: 640px;
  }
  .podcast-title {
    position: absolute;
    left: 0;
    top: 640px;
    width: 1156px;
    margin: 0;
    font-family: "Crimson Pro", "Times New Roman", serif;
    font-weight: 700;
    color: var(--title-red);
    text-align: center;
    text-transform: uppercase;
  }
  .podcast-title span {
    display: block;
    line-height: 1;
  }
  .title-main {
    font-size: 176px;
    letter-spacing: 2px;
  }
  .title-joiner {
    font-size: 118px;
    margin-top: -6px;
  }
  .title-end {
    font-size: 250px;
    margin-top: -22px;
    letter-spacing: 4px;
  }
</style>
</head>
<body>
  <main class="cover">
    <svg class="rope-heart" viewBox="0 0 1200 640" role="img" aria-label="Red and tan twisted rope tied into a heart shape, knotted onto a rope stretched across the cover">
      <defs>
        <linearGradient id="rope-tone" x1="0" y1="0" x2="1" y2="1">
          <stop offset="0" stop-color="var(--rope-red)"/>
          <stop offset="0.5" stop-color="var(--rope-tan)"/>
          <stop offset="1" stop-color="var(--rope-red)"/>
        </linearGradient>
      </defs>
      <rect x="368" y="176" width="440" height="400" rx="40" fill="url(#rope-tone)" opacity="0.55"/>
      <path d="M0 560 Q300 520 580 535 Q900 545 1200 615 L1200 600 Q900 530 580 522 Q300 510 0 548 Z" fill="url(#rope-tone)"/>
    </svg>

    <h1 class="podcast-title">
      <span class="title-main">Lanterns</span>
      <span class="title-joiner">at</span>
      <span class="title-end">Dusk</span>
    </h1>
  </main>
</body>
</html>
```